Design an exclusive flyer for a ski school that focuses on private lessons
Needs
Design a modern and engaging flyer for higher income customers. The flyer is intended to attract attention. The flyers are on the shelves at the ski pass counter. Since most flyers are very colorful with plenty of pictures, we would like to use clearer lines and less or no picture material. The ski school is in Sölden (Tyrol, Austria).
The dimensions should be that of a postcard (10.5cm x 14.8cm)
Front: - Logo (here you can also choose the colors freely)
- Private lessons
- learn differently
-Sölden
Back: should read the following in German and English ...
Private lessons (the better you drive, the more fun you have)
Private Lessons (the better you ride the more you enjoy)
For families & friends (finally going on vacation together)
Families & Friends (go on holidays together)
Freeride & ski tours (an unforgettable mountain experience)
Freeride & Ski Touring (pure mountain adventure)
QR Code (website)
www.peakvora.eu
which languages ​​we speak (German, Czech, English and Russian)
Phone number, whatsapp sign and soc.media signs

```html
<!DOCTYPE html>
<html lang="en">
<head>
<meta charset="utf-8">
<title>peakvora – ski &amp; snowboard school flyer</title>
<link rel="stylesheet" href="https://fonts.googleapis.com/css2?family=Montserrat:wght@400;500;700&family=Tinos:ital,wght@0,400;0,700;1,400&display=swap">
<style>
  :root{
    --backdrop:#e9edf1;
    --paper:#ffffff;
    --ink:#1d1d1f;
    --ink-soft:#3a3a3d;
    --grey:#9a9ca0;
    --grey-light:#dcdde0;
    --brand:#3d7fd6;
    --brand-deep:#1f5fae;
    --accent-red:#e0303a;
    --band-light:#6fa3e3;
  }
  *{box-sizing:border-box;margin:0;padding:0}
  html,body{width:1200px;height:968px;overflow:hidden;background:var(--backdrop)}
  .canvas{position:relative;width:1200px;height:968px}
  .flyer{position:absolute;top:104px;width:540px;height:760px;background:var(--paper);overflow:hidden;box-shadow:0 6px 18px rgba(0,0,0,.12)}
  .flyer--front{left:40px}
  .flyer--back{left:620px}

  /* shared logo */
  .logo{position:absolute;display:flex;align-items:center;gap:10px;font-family:Montserrat,sans-serif;font-weight:700;color:var(--brand)}
  .logo__dot{width:1em;height:1em;border-radius:50%;background:var(--brand)}

  /* front */
  .front-bars{position:absolute;left:26px;top:0}
  .flyer--front .logo{top:38px;right:40px;font-size:38px}
  .logo__tagline{position:absolute;top:88px;right:40px;font-family:Montserrat,sans-serif;font-size:14px;color:var(--brand)}
  .dot-field{position:absolute;background:var(--grey-light);opacity:.55}
  .dot-field--top{top:46px;left:150px;width:140px;height:20px}
  .dot-field--mid{top:440px;left:120px;width:110px;height:34px}
  .dot-field--back{top:600px;left:60px;width:110px;height:18px}
  .front-claims{position:absolute;top:200px;left:110px;padding-left:16px;border-left:3px solid var(--ink);font-family:Montserrat,sans-serif;font-weight:500;font-size:24px;line-height:1.5;color:var(--ink)}
  .front-claims p:last-child{margin-top:22px}
  .front-claims .initial{color:var(--brand)}
  .front-scene{position:absolute;left:0;top:330px;width:540px;height:430px}

  /* back */
  .flyer--back .logo{top:26px;right:40px;font-size:22px}
  .back-side-bar{position:absolute;left:0;width:12px;background:var(--brand)}
  .back-side-bar--a{top:120px;height:40px}
  .back-side-bar--b{top:300px;height:60px;background:var(--band-light)}
  .back-side-bar--c{top:470px;height:30px}
  .offers{position:absolute;top:110px;left:40px;right:0}
  .offer{margin-bottom:26px}
  .offer__de{font-family:Tinos,serif;font-size:17px;color:var(--ink);padding:0 0 6px 8px}
  .offer__de strong{font-family:Montserrat,sans-serif;font-weight:500;font-size:14px;color:var(--brand);letter-spacing:.02em;margin-right:6px}
  .offer__en{font-family:Tinos,serif;font-size:17px;color:#fff;background:var(--ink);padding:7px 30px 7px 40px;margin-left:20px;clip-path:polygon(0 0,100% 0,96% 100%,0 100%)}
  .offer__en strong{font-family:Montserrat,sans-serif;font-weight:700;font-size:15px;margin-right:6px}
  .offer__en em{color:var(--band-light)}
  .offer--families .offer__en{background:var(--band-light)}
  .offer--families .offer__en em{color:var(--ink)}
  .languages{position:absolute;top:470px;left:40px;font-family:Tinos,serif;font-size:16px;color:var(--ink)}
  .languages__tag{display:inline-block;background:var(--accent-red);color:#fff;font-family:Montserrat,sans-serif;font-weight:700;font-size:10px;text-transform:uppercase;padding:3px 6px;margin-bottom:4px}
  .back-scene{position:absolute;left:0;top:540px;width:540px;height:120px}
  .contact{position:absolute;left:30px;right:30px;bottom:30px;height:60px}
  .contact__phone{position:absolute;left:0;top:0;display:flex;align-items:center;gap:10px;font-family:Tinos,serif;font-size:22px;color:var(--brand-deep)}
  .socials{position:absolute;right:40px;top:2px;display:flex;gap:8px}
  .socials span{width:18px;height:18px;border-radius:50%}
  .contact__web{position:absolute;right:10px;bottom:0;font-family:Tinos,serif;font-size:24px;color:var(--brand-deep)}
</style>
</head>
<body>
<main class="canvas">

  <section class="flyer flyer--front" aria-label="Flyer front">
    <svg class="front-bars" width="110" height="120" viewBox="0 0 110 120" aria-hidden="true">
      <rect x="0" y="0" width="10" height="110" fill="#1d1d1f"/>
      <rect x="20" y="0" width="10" height="80" fill="#1d1d1f"/>
      <rect x="40" y="0" width="18" height="50" fill="#3a3a3d"/>
      <rect x="68" y="0" width="6" height="30" fill="#9a9ca0"/>
    </svg>
    <div class="dot-field dot-field--top" role="img" aria-label="Dotted pattern"></div>

    <div class="logo"><span class="logo__dot"></span>peakvora</div>
    <p class="logo__tagline">ski &amp; snowboard school</p>

    <div class="front-claims">
      <p><span class="initial">P</span>rivate lessons</p>
      <p><span class="initial">L</span>earn differenty</p>
      <p><span class="initial">S</span>ölden</p>
    </div>

    <svg class="front-scene" viewBox="0 0 540 430" role="img" aria-label="Geometric mountain range with a skier carving down a curved slope">
      <defs>
        <linearGradient id="front-scene-fill" x1="0" y1="0" x2="0" y2="1">
          <stop offset="0" stop-color="#3a3a3d"/>
          <stop offset=".6" stop-color="#9a9ca0"/>
          <stop offset="1" stop-color="#e6e7e9"/>
        </linearGradient>
      </defs>
      <rect x="0" y="0" width="540" height="430" fill="url(#front-scene-fill)"/>
    </svg>
    <div class="dot-field dot-field--mid" role="img" aria-label="Dotted pattern"></div>
  </section>

  <section class="flyer flyer--back" aria-label="Flyer back">
    <div class="logo"><span class="logo__dot"></span>peakvora</div>

    <span class="back-side-bar back-side-bar--a"></span>
    <span class="back-side-bar back-side-bar--b"></span>
    <span class="back-side-bar back-side-bar--c"></span>

    <div class="offers">
      <div class="offer offer--private">
        <p class="offer__de"><strong>PRIVATUNTERRICHT</strong>“Je besser du fährst, desto mehr Spaß hast du”</p>
        <p class="offer__en"><strong>PRIVATE LESSONS</strong><em>“the better you ride the more you enjoy”</em></p>
      </div>
      <div class="offer offer--families">
        <p class="offer__de"><strong>FÜR FAMILIEN &amp; FREUNDE</strong>“endlich gemeinsam in den Urlaub”</p>
        <p class="offer__en"><strong>FAMILIES &amp; FRIENDS</strong><em>“go on holidays together”</em></p>
      </div>
      <div class="offer offer--freeride">
        <p class="offer__de"><strong>FREERIDE &amp; SKI TOURS</strong>“ein unvergessliches Bergerlebnis”</p>
        <p class="offer__en"><strong>FREERIDE &amp; TOURING</strong><em>“pure mountain adventure”</em></p>
      </div>
    </div>

    <div class="languages">
      <span class="languages__tag">We speak</span>
      <p>German, Czech, English and Russian</p>
    </div>

    <svg class="back-scene" viewBox="0 0 540 120" role="img" aria-label="Geometric mountain range">
      <defs>
        <linearGradient id="back-scene-fill" x1="0" y1="0" x2="0" y2="1">
          <stop offset="0" stop-color="#9a9ca0"/>
          <stop offset="1" stop-color="#2a2a2d"/>
        </linearGradient>
      </defs>
      <rect x="0" y="0" width="540" height="120" fill="url(#back-scene-fill)"/>
    </svg>
    <div class="dot-field dot-field--back" role="img" aria-label="Dotted pattern"></div>

    <div class="contact">
      <p class="contact__phone">
        <svg width="22" height="22" viewBox="0 0 24 24" aria-hidden="true">
          <circle cx="12" cy="12" r="12" fill="#1f5fae"/>
          <path d="M8.5 6.5l2 2.2-1.2 1.6a8 8 0 0 0 4.4 4.4l1.6-1.2 2.2 2-1.3 1.8c-4.6-.4-9-4.8-9.4-9.4z" fill="#fff"/>
        </svg>
        +43 660 512 47 08
      </p>
      <div class="socials" aria-label="Social media">
        <span style="background:#1f5fae"></span>
        <span style="background:#e0303a"></span>
        <span style="background:#8a3fb0"></span>
        <span style="background:#3d9be0"></span>
      </div>
      <p class="contact__web">www.peakvora.eu</p>
    </div>
  </section>

</main>
</body>
</html>
```